label design for soy candle

I am a start up making soy candles and other products involving scents.
On the label should be in writing : the scent, Handgemacht in der Schweiz, Sojakerze, my logo with the name Thorvel Candles on it. I will upload the currant label of my candles, but I want something more fashioned. The color of the label should be black with the scent written in gold, and the rest in white. Or maybe suggest something different, I am open to new designs. I am also open to change the logo, except the flower has to stay.
Sizes : square 60x60mm / round 50mm / rectangle 70x20mm ( for different jars )

```html
<!DOCTYPE html>
<html lang="de">
<head>
<meta charset="utf-8">
<title>Thorvel Candles – Sojakerze Label</title>
<link rel="stylesheet" href="https://fonts.googleapis.com/css2?family=Poiret+One&family=Kaushan+Script&display=swap">
<style>
  :root {
    --label-black: #0e0e0e;
    --frame-gold: #d8ae35;
    --scent-gold: #d9b038;
    --cream: #f4e4b4;
    --text-cream: #efe0b0;
  }
  html, body {
    margin: 0;
    padding: 0;
    width: 1200px;
    height: 1200px;
    overflow: hidden;
    background: var(--frame-gold);
  }
  .label {
    position: relative;
    width: 1200px;
    height: 1200px;
    box-sizing: border-box;
    border: 20px solid var(--frame-gold);
    background: var(--label-black);
    overflow: hidden;
  }
  .brand-mark {
    position: absolute;
    left: 50%;
    top: 150px;
    width: 60px;
    height: 60px;
    margin-left: -30px;
    border-radius: 50%;
    background: var(--cream);
  }
  .brand-rule {
    position: absolute;
    left: 234px;
    top: 273px;
    width: 682px;
    height: 5px;
    background: var(--cream);
  }
  .brand-name {
    position: absolute;
    left: 0;
    right: 0;
    top: 310px;
    margin: 0;
    text-align: center;
    font-family: "Poiret One", sans-serif;
    font-weight: 400;
    font-size: 132px;
    line-height: 1.2;
    color: var(--cream);
    white-space: nowrap;
  }
  .scent-name {
    position: absolute;
    left: 0;
    right: 0;
    top: 540px;
    margin: 0;
    text-align: center;
    font-family: "Kaushan Script", cursive;
    font-weight: 400;
    font-size: 240px;
    line-height: 1.2;
    color: var(--scent-gold);
    transform: rotate(-4deg);
  }
  .product-type {
    position: absolute;
    left: 0;
    right: 0;
    top: 938px;
    margin: 0;
    text-align: center;
    font-family: "Poiret One", sans-serif;
    font-size: 58px;
    letter-spacing: 0.12em;
    line-height: 1.2;
    color: var(--text-cream);
  }
  .origin {
    position: absolute;
    left: 0;
    right: 0;
    top: 1010px;
    margin: 0;
    text-align: center;
    font-family: "Poiret One", sans-serif;
    font-size: 62px;
    letter-spacing: 0.1em;
    line-height: 1.2;
    color: var(--text-cream);
    white-space: nowrap;
  }
</style>
</head>
<body>
  <main class="label">
    <div class="brand-mark" aria-hidden="true"></div>
    <div class="brand-rule" aria-hidden="true"></div>
    <h1 class="brand-name">Thorvel Candles</h1>
    <p class="scent-name">Scent</p>
    <p class="product-type">SOJAKERZE</p>
    <p class="origin">Handgemacht in der Schweiz</p>
  </main>
</body>
</html>
```